Redesign Comparisson chart - make modern and effective

Use your imaginations to make a powerful distinction between KRV & other holistic modalities. There are 7 elements physical, mental, emotional, energetic, subconscious, superconscious and before and after testing.
We want it to be obvious that KRV is the only modality that works on all these elements simultaneously. We do not want to include any chakras as we want this information to be accepted by a wide range of people and belief systems.'

We want it to look simple but effective. Professional but powerful. We want KRV to stand out even of you eye just passed over i.
Updates

Hi everyone, thanks for your submissions so far. Basically what this image is meant to represent is a comparison chart between all the modalities There are 5 elements physical, mental, emotional, subconscious and superconscious. we want to reflect that KRV is the only modality that works on all these elements simultaneously. As we want the concept to be accepted and not considered woo woo, we want to steer away from chakras.

Target Market(s)

Professionals

Industry/Entity Type

Professional services

Font styles to use
Sans Serif
Other font styles liked:
• Poppins Monserratt

Colors
0094D4
00A9DD
6FCCEA
C7EBF8
E9F6FB

Requirements
Must have
• Clear/professional and clean look. Brand colours and logos. All typography and formats must be cohesive.
Nice to have
• More easy to read, different layout
Should not have
• Do not change the data just the way its presented. No chakras

```html
<!DOCTYPE html>
<html lang="en">
<head>
<meta charset="utf-8">
<title>KRV Method – Modality Comparison</title>
<link href="https://fonts.googleapis.com/css2?family=Montserrat:wght@500;700&family=Roboto+Slab:wght@600;700&family=Roboto:wght@400&display=swap" rel="stylesheet">
<style>
  :root{
    --brand:#3bb9e6;
    --band:#117ea8;
    --cell:#e7f5fb;
    --label:#2c88b4;
    --divider:#4d8fb5;
    --ink:#222;
    --body:#4a4a4a;
    --physical:#d9413f;
    --mental:#5bbfe0;
    --emotional:#5aa844;
    --energetic:#f59a23;
    --sub:#f2cf1a;
    --super:#7c5ea8;
    --testing:#d665a8;
  }
  *{box-sizing:border-box;margin:0;padding:0}
  html,body{width:1200px;height:1008px;overflow:hidden;background:#fff}
  .canvas{position:relative;width:1200px;height:1008px;font-family:Roboto,Arial,sans-serif}

  /* header */
  .masthead{position:absolute;left:0;top:0;width:1200px;height:77px;background:#fff}
  .brand-name{position:absolute;left:212px;top:27px;font-family:Montserrat,sans-serif;font-weight:700;color:var(--brand);font-size:18px;line-height:22px;white-space:nowrap}
  .headline{position:absolute;left:350px;width:650px;top:11px;text-align:center}
  .headline h1{font-family:Montserrat,sans-serif;font-weight:700;font-size:18px;color:var(--brand);letter-spacing:.2px}
  .headline p{font-family:Montserrat,sans-serif;font-weight:500;font-size:10px;line-height:12.6px;color:#111;margin-top:3px}

  /* chart band */
  .band{position:absolute;left:0;top:77px;width:1200px;height:782px;background:var(--band)}
  .col-heads{position:absolute;left:334px;top:91px;width:746px;height:43px;background:var(--cell);border-radius:3px;display:grid;grid-template-columns:repeat(7,1fr)}
  .col-head{position:relative;display:flex;align-items:center;justify-content:center;text-align:center;font-family:"Roboto Slab",serif;font-weight:700;font-size:12px;line-height:13.5px}
  .col-head+.col-head::before,.cell+.cell::before{content:"";position:absolute;left:0;top:14%;bottom:14%;border-left:1.5px solid var(--divider)}
  .c-physical{color:var(--physical)} .c-mental{color:var(--mental)} .c-emotional{color:var(--emotional)}
  .c-energetic{color:var(--energetic)} .c-sub{color:var(--sub)} .c-super{color:var(--super)} .c-testing{color:var(--testing)}

  .rows{position:absolute;left:121px;top:139px;width:959px;display:flex;flex-direction:column;gap:5.4px}
  .row{display:grid;grid-template-columns:208px 746px;column-gap:5px}
  .modality{background:var(--cell);border-radius:3px;display:flex;flex-direction:column;justify-content:center;padding-left:18px;font-family:"Roboto Slab",serif;font-weight:700;font-size:13px;line-height:15.6px;color:var(--label)}
  .cells{background:var(--cell);border-radius:3px;display:grid;grid-template-columns:repeat(7,1fr)}
  .cell{position:relative;display:flex;align-items:center;justify-content:center}
  .tick{width:18px;height:18px;fill:none;stroke-width:3;stroke-linecap:round;stroke-linejoin:round}
  .h1{height:86px}.h2{height:26.5px}.h3{height:42px}

  .row-featured{height:61px;grid-template-columns:250px 787px;margin-left:-42px}
  .row-featured .modality,.row-featured .cells{background:#fff;border-radius:6px}
  .row-featured .modality{padding-left:111px;color:var(--ink);font-size:14px;line-height:17px}
  .row-featured .cells{grid-template-columns:repeat(7,106.5px)}
  .row-featured .tick{width:32px;height:32px;stroke-width:4.5}

  /* legend */
  .legend{position:absolute;top:866px;left:0;width:1200px}
  .legend-col{position:absolute;top:0}
  .legend h2{font-family:"Roboto Slab",serif;font-weight:700;font-size:13.5px;display:flex;align-items:center;gap:8px;margin-bottom:4px}
  .legend h2::before{content:"";width:8px;height:8px;background:currentColor;transform:rotate(45deg)}
  .legend p{font-size:10.4px;line-height:12.6px;color:var(--body);text-align:justify;margin-bottom:7px}
  .credit{position:absolute;left:2px;top:108px;display:flex;align-items:center;gap:7px;font-family:Montserrat,sans-serif;white-space:nowrap}
  .credit-name{font-weight:700;font-size:12.5px;color:var(--brand)}
  .credit-url{font-weight:500;font-size:8.5px;color:var(--brand);border-left:1px solid var(--brand);padding-left:6px}
</style>
</head>
<body>
<svg width="0" height="0" style="position:absolute">
  <defs><symbol id="tick" viewBox="0 0 24 24"><path d="M4 12.5 L9.5 18 L20.5 5"/></symbol></defs>
</svg>
<div class="canvas">
  <header class="masthead">
    <div class="brand-name">KRV Method</div>
    <div class="headline">
      <h1>Choose KRV for Fast, Immediate and Powerful Results</h1>
      <p>I must experience healing on all levels, I am not just a body. I want to learn how to heal myself, so I’m not dependent on others.<br>I want to release all my emotional and mental blocks, so I can be the best version of myself.</p>
    </div>
  </header>

  <section class="band" aria-label="Modality comparison chart"></section>
  <div class="col-heads">
    <div class="col-head c-physical">PHYSICAL</div>
    <div class="col-head c-mental">MENTAL</div>
    <div class="col-head c-emotional">EMOTIONAL</div>
    <div class="col-head c-energetic">ENERGETIC</div>
    <div class="col-head c-sub">SUB<br>CONSCIOUS</div>
    <div class="col-head c-super">SUPER<br>CONSCIOUS</div>
    <div class="col-head c-testing">BEFORE &amp;<br>AFTER TESTING</div>
  </div>

  <div class="rows">
    <div class="row h1"><div class="modality">MASSAGE<br>YOGA<br>NATROPATHY<br>AYURVEDIC MEDICINE<br>WESTERN MEDICINE</div>
      <div class="cells"><div class="cell"><svg class="tick" stroke="var(--physical)"><use href="#tick"/></svg></div><div class="cell"></div><div class="cell"></div><div class="cell"></div><div class="cell"></div><div class="cell"></div><div class="cell"></div></div></div>
    <div class="row h2"><div class="modality">PSYCHIC INTUITIVE</div>
      <div class="cells"><div class="cell"><svg class="tick" stroke="var(--physical)"><use href="#tick"/></svg></div><div class="cell"><svg class="tick" stroke="var(--mental)"><use href="#tick"/></svg></div><div class="cell"></div><div class="cell"></div><div class="cell"></div><div class="cell"></div><div class="cell"></div></div></div>
    <div class="row h2"><div class="modality">FAMILY CONSTELLATION</div>
      <div class="cells"><div class="cell"><svg class="tick" stroke="var(--physical)"><use href="#tick"/></svg></div><div class="cell"><svg class="tick" stroke="var(--mental)"><use href="#tick"/></svg></div><div class="cell"></div><div class="cell"><svg class="tick" stroke="var(--energetic)"><use href="#tick"/></svg></div><div class="cell"></div><div class="cell"></div><div class="cell"></div></div></div>
    <div class="row h2"><div class="modality">ACUPUNCTURE</div>
      <div class="cells"><div class="cell"><svg class="tick" stroke="var(--physical)"><use href="#tick"/></svg></div><div class="cell"></div><div class="cell"></div><div class="cell"><svg class="tick" stroke="var(--energetic)"><use href="#tick"/></svg></div><div class="cell"></div><div class="cell"></div><div class="cell"></div></div></div>
    <div class="row h2"><div class="modality">NUTRITIONAL HEALING</div>
      <div class="cells"><div class="cell"><svg class="tick" stroke="var(--physical)"><use href="#tick"/></svg></div><div class="cell"></div><div class="cell"></div><div class="cell"></div><div class="cell"></div><div class="cell"></div><div class="cell"><svg class="tick" stroke="var(--testing)"><use href="#tick"/></svg></div></div></div>
    <div class="row h2"><div class="modality">CHINESE MEDICINE</div>
      <div class="cells"><div class="cell"><svg class="tick" stroke="var(--physical)"><use href="#tick"/></svg></div><div class="cell"></div><div class="cell"></div><div class="cell"><svg class="tick" stroke="var(--energetic)"><use href="#tick"/></svg></div><div class="cell"></div><div class="cell"></div><div class="cell"><svg class="tick" stroke="var(--testing)"><use href="#tick"/></svg></div></div></div>
    <div class="row h3"><div class="modality">KINESIOLOGY<br>BOWEN THERAPY</div>
      <div class="cells"><div class="cell"><svg class="tick" stroke="var(--physical)"><use href="#tick"/></svg></div><div class="cell"></div><div class="cell"></div><div class="cell"></div><div class="cell"><svg class="tick" stroke="var(--sub)"><use href="#tick"/></svg></div><div class="cell"></div><div class="cell"><svg class="tick" stroke="var(--testing)"><use href="#tick"/></svg></div></div></div>

    <div class="row row-featured"><div class="modality">KRV<br>METHOD</div>
      <div class="cells">
        <div class="cell"><svg class="tick" stroke="var(--physical)"><use href="#tick"/></svg></div>
        <div class="cell"><svg class="tick" stroke="var(--mental)"><use href="#tick"/></svg></div>
        <div class="cell"><svg class="tick" stroke="var(--emotional)"><use href="#tick"/></svg></div>
        <div class="cell"><svg class="tick" stroke="var(--energetic)"><use href="#tick"/></svg></div>
        <div class="cell"><svg class="tick" stroke="var(--sub)"><use href="#tick"/></svg></div>
        <div class="cell"><svg class="tick" stroke="var(--super)"><use href="#tick"/></svg></div>
        <div class="cell"><svg class="tick" stroke="var(--testing)"><use href="#tick"/></svg></div>
      </div></div>

    <div class="row h2"><div class="modality">EFT</div>
      <div class="cells"><div class="cell"><svg class="tick" stroke="var(--physical)"><use href="#tick"/></svg></div><div class="cell"><svg class="tick" stroke="var(--mental)"><use href="#tick"/></svg></div><div class="cell"></div><div class="cell"></div><div class="cell"><svg class="tick" stroke="var(--sub)"><use href="#tick"/></svg></div><div class="cell"></div><div class="cell"><svg class="tick" stroke="var(--testing)"><use href="#tick"/></svg></div></div></div>
    <div class="row h2"><div class="modality">CHIROPRACTIC</div>
      <div class="cells"><div class="cell"><svg class="tick" stroke="var(--physical)"><use href="#tick"/></svg></div><div class="cell"></div><div class="cell"></div><div class="cell"><svg class="tick" stroke="var(--energetic)"><use href="#tick"/></svg></div><div class="cell"></div><div class="cell"></div><div class="cell"><svg class="tick" stroke="var(--testing)"><use href="#tick"/></svg></div></div></div>
    <div class="row h3"><div class="modality">REIKI<br>CRYSTAL HEALING</div>
      <div class="cells"><div class="cell"></div><div class="cell"></div><div class="cell"></div><div class="cell"><svg class="tick" stroke="var(--energetic)"><use href="#tick"/></svg></div><div class="cell"></div><div class="cell"></div><div class="cell"></div></div></div>
    <div class="row h2"><div class="modality">ENERGY MEDICINE</div>
      <div class="cells"><div class="cell"></div><div class="cell"></div><div class="cell"></div><div class="cell"><svg class="tick" stroke="var(--energetic)"><use href="#tick"/></svg></div><div class="cell"></div><div class="cell"></div><div class="cell"><svg class="tick" stroke="var(--testing)"><use href="#tick"/></svg></div></div></div>
    <div class="row h2"><div class="modality">THETA HEALING</div>
      <div class="cells"><div class="cell"></div><div class="cell"></div><div class="cell"></div><div class="cell"></div><div class="cell"><svg class="tick" stroke="var(--sub)"><use href="#tick"/></svg></div><div class="cell"><svg class="tick" stroke="var(--super)"><use href="#tick"/></svg></div><div class="cell"></div></div></div>
    <div class="row h2"><div class="modality">PSYCHOLOGY</div>
      <div class="cells"><div class="cell"></div><div class="cell"><svg class="tick" stroke="var(--mental)"><use href="#tick"/></svg></div><div class="cell"></div><div class="cell"></div><div class="cell"></div><div class="cell"></div><div class="cell"></div></div></div>
    <div class="row h3"><div class="modality">MINDFULNESS MEDITATION<br>LIFE COACHING</div>
      <div class="cells"><div class="cell"></div><div class="cell"><svg class="tick" stroke="var(--mental)"><use href="#tick"/></svg></div><div class="cell"></div><div class="cell"></div><div class="cell"></div><div class="cell"></div><div class="cell"><svg class="tick" stroke="var(--testing)"><use href="#tick"/></svg></div></div></div>
    <div class="row h3"><div class="modality">HYPNOTHERAPY<br>INNER CHILD HEALING</div>
      <div class="cells"><div class="cell"></div><div class="cell"><svg class="tick" stroke="var(--mental)"><use href="#tick"/></svg></div><div class="cell"></div><div class="cell"></div><div class="cell"><svg class="tick" stroke="var(--sub)"><use href="#tick"/></svg></div><div class="cell"></div><div class="cell"></div></div></div>
    <div class="row h3"><div class="modality">NLP<br>TIMELINE THERAPY</div>
      <div class="cells"><div class="cell"></div><div class="cell"><svg class="tick" stroke="var(--mental)"><use href="#tick"/></svg></div><div class="cell"></div><div class="cell"></div><div class="cell"><svg class="tick" stroke="var(--sub)"><use href="#tick"/></svg></div><div class="cell"></div><div class="cell"><svg class="tick" stroke="var(--testing)"><use href="#tick"/></svg></div></div></div>
  </div>

  <footer class="legend">
    <div class="legend-col" style="left:62px;width:240px">
      <h2 class="c-physical">PHYSICAL</h2>
      <p>Most modalities, including a western medicine, focus on and treat the physical body only. The KRV process enables you to engage in healing your own body during the session. There is no muscle testing, no hands-on healing and no herbal remedies or medicines.</p>
      <div class="credit"><span class="credit-name">lumenwell</span><span class="credit-url">www.lumenwell.com.au</span></div>
    </div>
    <div class="legend-col" style="left:320px;width:247px">
      <h2 class="c-mental">MENTAL</h2>
      <p>KRV enables you to use your own consciousness to self-heal. We don’t give you advice or coaching, we allow your mind to heal itself.</p>
      <h2 class="c-energetic" style="margin-top:6px">ENERGETIC</h2>
      <p>Most modalities try to move the energy in your body for you. KRV enables and empowers you to do it yourself.</p>
    </div>
    <div class="legend-col" style="left:582px;width:276px">
      <h2 class="c-emotional">EMOTIONAL</h2>
      <p>KRV is the only modality that engages your emotions on a physical level. Emotions get stuck in your body and can cause illness over time if left unchecked. KRV enables you you experience fast and powerful emotional releasing</p>
      <h2 class="c-super">SUPERCONSCIOUS</h2>
      <p>KRV is the only modality the enables you to access and heal your superconscious mind yourself.</p>
    </div>
    <div class="legend-col" style="left:874px;width:268px">
      <h2 class="c-sub">SUBCONSCIOUS</h2>
      <p>Some modalities, like Kinesiology, access your subconscious through muscle testing. KRV empowers you to access your own subconscious and heal it yourself.</p>
      <h2 class="c-testing">BEFORE &amp; AFTER TESTING</h2>
      <p>KRV is the only modality the enables you to provide before and after results, which are documented by us, and analysed by you with our help.</p>
    </div>
  </footer>
</div>
</body>
</html>
```